Business Card Design Project - KLB

I am looking for a more sophisticated card design for my company,
"The Kestrel Bureau"

We are a consultancy focused on strategy and change in Associations and professional organisations.

I am a lawyer and psychologist with a PhD and so am looking for something that communicates seriousness and credibility but also quirky creative solutions for strategic problems, which is my field of speciality.

I am looking for something that is quietly spoken, rather than loud colours ('credible' and 'creative' are the two adjectives that I think of as competing here).

I particularly like an embossed card style - heavy white card with plain white or white and black or white and grey text.

The key logo image for the company is a question mark and I am open to suggestions and ideas on design.

I have attached a file that includes a couple of styles that have caught my eye and my thoughts on them. Hopefully they communicate what I'm looking for.
Updates

Thank you for all the great suggestions and designs.

I really appreciated the effort and creative energy you put into your designs. I have now closed the project after selecting a design and advising the successful designer of the card that I am happy with.

Regards

Target Market(s)

Organisations (CEO's and Boards), Governments, Legal professionals, Membership Associations and aspiring professionals.

Industry/Entity Type

Lawyer

Requirements
Must have
• The key logo element is a question mark (?) and this needs to be incorporated.

Embossed style - cut outs or other design ideas interest me too.

The attached file has a number of sample ideas and comments on each one that I like.
Should not have
• I like crisp, modern fonts (Myriads etc...) and do not like embellished fonts or Times etc...

```html
<!DOCTYPE html>
<html lang="en">
<head>
<meta charset="utf-8">
<title>The Kestrel Bureau – Business Card</title>
<link rel="stylesheet" href="https://fonts.googleapis.com/css2?family=Source+Sans+3:wght@400;600;700&display=swap">
<style>
  :root {
    --page: #ffffff;
    --grey-light: #4a4c50;
    --grey-dark: #232427;
    --black: #070708;
    --black-soft: #151618;
    --text-main: #d9dadc;
    --text-muted: #8a8c90;
    --divider: #2c2d30;
    --font: "Source Sans 3", "Helvetica Neue", Arial, sans-serif;
  }
  * { margin: 0; padding: 0; box-sizing: border-box; }
  html, body { width: 1200px; height: 830px; overflow: hidden; background: var(--page); }
  body { position: relative; font-family: var(--font); color: var(--text-main); }

  .spread { position: absolute; left: 10px; width: 1180px; }
  .spread--top { top: 30px; height: 336px; }
  .spread--bottom { top: 400px; height: 380px; }
  .spread__shape { position: absolute; inset: 0; width: 100%; height: 100%; }

  .card-face { position: absolute; }

  .wordmark {
    position: absolute;
    font-family: var(--font);
    font-weight: 600;
    color: var(--text-main);
    white-space: nowrap;
    letter-spacing: 0.5px;
    line-height: 1;
  }
  .wordmark--horizontal { font-size: 30px; }
  .wordmark--vertical {
    font-size: 26px;
    transform: rotate(-90deg);
    transform-origin: left top;
  }

  .holder { position: absolute; text-align: right; white-space: nowrap; }
  .holder__name {
    font-size: 15px; font-weight: 700; letter-spacing: 0.3px;
    color: var(--text-main);
  }
  .holder__title {
    display: block; font-size: 6px; font-weight: 600; letter-spacing: 0.8px;
    color: var(--text-muted); text-transform: uppercase; margin-top: -2px;
  }
  .holder__web {
    display: block; font-size: 10px; letter-spacing: 1px;
    color: var(--text-muted); margin-top: 6px;
  }

  .divider { position: absolute; width: 1px; background: var(--divider); }

  .contact { position: absolute; white-space: nowrap; }
  .contact__honorific {
    position: absolute; left: 0; top: 0;
    font-size: 11px; font-weight: 700; color: var(--text-muted);
  }
  .contact__row {
    position: absolute; left: 0; height: 14px;
    display: flex; align-items: center;
    font-size: 9.5px; font-weight: 700; letter-spacing: 0.4px;
    color: var(--text-main); text-transform: uppercase;
  }
  .contact__icon { width: 12px; height: 12px; margin-right: 26px; flex: none; }
  .contact__icon path, .contact__icon rect, .contact__icon circle { fill: var(--text-muted); }
  .contact__row--name .contact__label { margin-left: 38px; }
</style>
</head>
<body>

<!-- Top spread: front on the left, back on the right -->
<section class="spread spread--top" aria-label="Card spread, front and back">
  <svg class="spread__shape" viewBox="0 0 1180 336" preserveAspectRatio="none" aria-hidden="true">
    <defs>
      <linearGradient id="greyTop" x1="0" y1="0" x2="0" y2="1">
        <stop offset="0" stop-color="#3c3e42"/>
        <stop offset="0.5" stop-color="#1f2023"/>
        <stop offset="1" stop-color="#45474b"/>
      </linearGradient>
      <radialGradient id="blackGlowTop" cx="0.5" cy="0.5" r="0.6">
        <stop offset="0" stop-color="#1b1c1f"/>
        <stop offset="1" stop-color="#050506"/>
      </radialGradient>
    </defs>
    <rect width="1180" height="336" fill="url(#greyTop)"/>
    <path d="M0,84 Q300,60 590,0 L590,336 Q300,290 0,270 Z" fill="url(#blackGlowTop)"/>
    <path d="M590,0 Q880,60 1180,84 L1180,270 Q880,290 590,336 Z" fill="url(#blackGlowTop)"/>
    <line x1="590" y1="0" x2="590" y2="336" stroke="#000" stroke-width="2"/>
  </svg>

  <!-- Front face -->
  <div class="card-face" style="left:0; top:0; width:590px; height:336px;">
    <div class="holder" style="right:320px; top:144px;">
      <span class="holder__name">MARA ELLISON</span>
      <span class="holder__title">Director</span>
      <span class="holder__web">WWW.KESTRELBUREAU.COM</span>
    </div>
    <div class="divider" style="left:278px; top:110px; height:130px;"></div>
    <div class="wordmark wordmark--horizontal" style="left:294px; top:158px;">The Kestrel Bureau</div>
  </div>

  <!-- Back face -->
  <div class="card-face" style="left:590px; top:0; width:590px; height:336px;">
    <div class="wordmark wordmark--vertical" style="left:96px; top:290px;">The Kestrel Bureau</div>
    <div class="divider" style="left:172px; top:96px; height:190px;"></div>
    <div class="contact" style="left:186px; top:110px;">
      <span class="contact__honorific">DR.</span>
      <div class="contact__row contact__row--name" style="top:0;"><span class="contact__label">MARA ELLISON</span></div>
      <div class="contact__row" style="top:22px;">
        <svg class="contact__icon" viewBox="0 0 12 12" aria-hidden="true"><rect x="0" y="2" width="12" height="3" rx="1"/><rect x="2" y="5" width="8" height="6" rx="1"/></svg>
        <span>+614.0555.0187</span>
      </div>
      <div class="contact__row" style="top:46px;">
        <svg class="contact__icon" viewBox="0 0 12 12" aria-hidden="true"><rect x="0" y="2" width="12" height="3" rx="1"/><rect x="2" y="5" width="8" height="6" rx="1"/></svg>
        <span>+612.5550.1832</span>
      </div>
      <div class="contact__row" style="top:70px;">
        <svg class="contact__icon" viewBox="0 0 12 12" aria-hidden="true"><path d="M0,2 H12 V10 H0 Z M1,3 L6,7 L11,3 Z" fill-rule="evenodd"/></svg>
        <span>MARA@KESTRELBUREAU.COM.AU</span>
      </div>
      <div class="contact__row" style="top:96px;">
        <svg class="contact__icon" viewBox="0 0 12 12" aria-hidden="true"><path d="M6,0 C3.8,0 2.5,1.6 2.5,3.6 C2.5,6.2 6,12 6,12 C6,12 9.5,6.2 9.5,3.6 C9.5,1.6 8.2,0 6,0 Z M6,2.3 A1.4,1.4 0 1 1 6,5.1 A1.4,1.4 0 1 1 6,2.3 Z" fill-rule="evenodd"/></svg>
        <span>P.O. BOX 4410, ELM GROVE, SYDNEY, AUSTRALIA</span>
      </div>
    </div>
  </div>
</section>

<!-- Bottom spread: back on the left, front on the right -->
<section class="spread spread--bottom" aria-label="Card spread, back and front">
  <svg class="spread__shape" viewBox="0 0 1180 380" preserveAspectRatio="none" aria-hidden="true">
    <defs>
      <linearGradient id="greyBottom" x1="0" y1="0" x2="0" y2="1">
        <stop offset="0" stop-color="#4a4c50"/>
        <stop offset="0.5" stop-color="#202124"/>
        <stop offset="1" stop-color="#4a4c50"/>
      </linearGradient>
      <radialGradient id="blackGlowBottom" cx="0.5" cy="0.5" r="0.6">
        <stop offset="0" stop-color="#18191c"/>
        <stop offset="1" stop-color="#050506"/>
      </radialGradient>
    </defs>
    <rect width="1180" height="380" fill="url(#greyBottom)"/>
    <rect width="1180" height="30" fill="#55575b"/>
    <rect y="358" width="1180" height="22" fill="#55575b"/>
    <path d="M0,30 Q300,70 590,100 Q880,70 1180,30 L1180,358 Q880,300 590,290 Q300,300 0,358 Z" fill="url(#blackGlowBottom)"/>
  </svg>

  <!-- Back face -->
  <div class="card-face" style="left:0; top:0; width:590px; height:380px;">
    <div class="wordmark wordmark--vertical" style="left:98px; top:296px;">The Kestrel Bureau</div>
    <div class="divider" style="left:176px; top:110px; height:190px;"></div>
    <div class="contact" style="left:190px; top:134px;">
      <span class="contact__honorific">DR.</span>
      <div class="contact__row contact__row--name" style="top:0;"><span class="contact__label">MARA ELLISON</span></div>
      <div class="contact__row" style="top:22px;">
        <svg class="contact__icon" viewBox="0 0 12 12" aria-hidden="true"><rect x="0" y="2" width="12" height="3" rx="1"/><rect x="2" y="5" width="8" height="6" rx="1"/></svg>
        <span>+614.0555.0187</span>
      </div>
      <div class="contact__row" style="top:46px;">
        <svg class="contact__icon" viewBox="0 0 12 12" aria-hidden="true"><rect x="0" y="2" width="12" height="3" rx="1"/><rect x="2" y="5" width="8" height="6" rx="1"/></svg>
        <span>+612.5550.1832</span>
      </div>
      <div class="contact__row" style="top:70px;">
        <svg class="contact__icon" viewBox="0 0 12 12" aria-hidden="true"><path d="M0,2 H12 V10 H0 Z M1,3 L6,7 L11,3 Z" fill-rule="evenodd"/></svg>
        <span>MARA@KESTRELBUREAU.COM.AU</span>
      </div>
      <div class="contact__row" style="top:96px;">
        <svg class="contact__icon" viewBox="0 0 12 12" aria-hidden="true"><path d="M6,0 C3.8,0 2.5,1.6 2.5,3.6 C2.5,6.2 6,12 6,12 C6,12 9.5,6.2 9.5,3.6 C9.5,1.6 8.2,0 6,0 Z M6,2.3 A1.4,1.4 0 1 1 6,5.1 A1.4,1.4 0 1 1 6,2.3 Z" fill-rule="evenodd"/></svg>
        <span>P.O. BOX 4410, ELM GROVE, SYDNEY, AUSTRALIA</span>
      </div>
    </div>
  </div>

  <!-- Front face -->
  <div class="card-face" style="left:590px; top:0; width:590px; height:380px;">
    <div class="holder" style="right:354px; top:168px;">
      <span class="holder__name">MARA ELLISON</span>
      <span class="holder__title">Director</span>
      <span class="holder__web">WWW.KESTRELBUREAU.COM</span>
    </div>
    <div class="divider" style="left:246px; top:130px; height:130px;"></div>
    <div class="wordmark wordmark--horizontal" style="left:262px; top:180px;">The Kestrel Bureau</div>
  </div>
</section>

</body>
</html>
```